Luminar Optics

I wish to make a mailing of a postcard format to pathologists in the UK. Probable number between 500 and 1000.There are 3 elements. 1. A small number of words (about 12) 2. A picture of our product 3. A relevant (tissue section) background. I have knocked up a rough idea of what I want ... BUT ... I'm obviously not a designer. The text looks awful and needs some way of standing out (and being legible) against the background. I can send original images of product and background. Important ... Aspect ratios of images must not be changed.
Look and feel
Each slider illustrates characteristics of the customer's brand and the style your logo design should communicate.

```html
<!DOCTYPE html>
<html lang="en">
<head>
<meta charset="utf-8">
<title>Luminar Optics – Whole Slide Scanning Postcard</title>
<link href="https://fonts.googleapis.com/css2?family=Open+Sans:wght@300;400;600&display=swap" rel="stylesheet">
<style>
  :root {
    --page-bg: #d9d9d9;
    --card-white: #f4f4f4;
    --card-white-edge: #e6e6e6;
    --tissue-pink: #c4577f;
    --tissue-rose: #d9809f;
    --tissue-purple: #6d3c86;
    --tissue-light: #ecc2d3;
    --brand-purple: #5b4a9e;
    --text-dark: #1e1e1e;
    --text-grey: #5a5a5a;
    --text-soft: #7a7a7a;
    --device-light: #fbfbfb;
    --device-shade: #d4d4d4;
  }
  * { margin: 0; padding: 0; box-sizing: border-box; }
  html, body {
    width: 1200px;
    height: 953px;
    overflow: hidden;
    background: var(--page-bg);
    font-family: "Open Sans", Arial, sans-serif;
  }
  .postcard {
    position: absolute;
    left: 40px;
    top: 48px;
    width: 1120px;
    height: 856px;
    background: radial-gradient(ellipse at 65% 50%, #ffffff 0%, var(--card-white) 55%, var(--card-white-edge) 100%);
    overflow: hidden;
  }
  .tissue-band {
    position: absolute;
    left: 0;
    width: 100%;
    background:
      radial-gradient(circle at 20% 40%, var(--tissue-purple) 0%, transparent 35%),
      radial-gradient(circle at 70% 60%, var(--tissue-purple) 0%, transparent 30%),
      radial-gradient(circle at 92% 40%, var(--tissue-light) 0%, transparent 22%),
      linear-gradient(100deg, var(--tissue-pink), var(--tissue-rose) 45%, var(--tissue-pink) 75%, var(--tissue-light));
  }
  .tissue-band--top { top: 0; height: 180px; }
  .tissue-band--bottom { top: 732px; height: 124px; }

  .brand {
    position: absolute;
    left: 28px;
    top: 226px;
    display: flex;
    align-items: center;
    gap: 14px;
  }
  .brand__square {
    width: 46px;
    height: 46px;
    background: var(--brand-purple);
  }
  .brand__name {
    font-size: 36px;
    font-weight: 600;
    color: var(--text-dark);
    letter-spacing: -0.3px;
  }

  .headline {
    position: absolute;
    left: 31px;
    top: 315px;
    font-size: 27px;
    font-weight: 300;
    color: var(--text-soft);
    letter-spacing: 0.2px;
  }

  .benefits {
    position: absolute;
    left: 57px;
    top: 395px;
    list-style: none;
  }
  .benefits__item {
    display: flex;
    align-items: center;
    height: 52.5px;
    font-size: 36px;
    font-weight: 400;
    color: var(--text-grey);
  }
  .benefits__tick {
    width: 26px;
    height: 22px;
    margin-right: 25px;
  }

  .web-address {
    position: absolute;
    left: 0;
    top: 647px;
    width: 452px;
    height: 59px;
    background: var(--brand-purple);
    color: #ffffff;
    font-size: 28px;
    font-weight: 300;
    line-height: 59px;
    padding-left: 25px;
  }

  .product-photo {
    position: absolute;
    left: 561px;
    top: 210px;
    width: 508px;
    height: 456px;
    border-radius: 60px 60px 40px 40px;
    background:
      radial-gradient(ellipse at 35% 30%, var(--device-light) 0%, #eeeeee 50%, var(--device-shade) 100%);
  }
</style>
</head>
<body>
  <main class="postcard">
    <div class="tissue-band tissue-band--top" role="img" aria-label="Stained tissue section micrograph in pink and purple"></div>

    <div class="brand">
      <span class="brand__square"></span>
      <span class="brand__name">Luminar Optics</span>
    </div>

    <p class="headline">WHOLE SLIDE SCANNING IS NOW ...</p>

    <ul class="benefits">
      <li class="benefits__item">
        <svg class="benefits__tick" viewBox="0 0 26 22" aria-hidden="true"><path d="M2 11 L10 19 L24 2" fill="none" stroke="#5b4a9e" stroke-width="3.5" stroke-linecap="round" stroke-linejoin="round"/></svg>
        COMPACT
      </li>
      <li class="benefits__item">
        <svg class="benefits__tick" viewBox="0 0 26 22" aria-hidden="true"><path d="M2 11 L10 19 L24 2" fill="none" stroke="#5b4a9e" stroke-width="3.5" stroke-linecap="round" stroke-linejoin="round"/></svg>
        SIMPLE
      </li>
      <li class="benefits__item">
        <svg class="benefits__tick" viewBox="0 0 26 22" aria-hidden="true"><path d="M2 11 L10 19 L24 2" fill="none" stroke="#5b4a9e" stroke-width="3.5" stroke-linecap="round" stroke-linejoin="round"/></svg>
        FAST
      </li>
      <li class="benefits__item">
        <svg class="benefits__tick" viewBox="0 0 26 22" aria-hidden="true"><path d="M2 11 L10 19 L24 2" fill="none" stroke="#5b4a9e" stroke-width="3.5" stroke-linecap="round" stroke-linejoin="round"/></svg>
        AFFORDABLE
      </li>
    </ul>

    <div class="web-address">www.luminaroptics.com</div>

    <div class="product-photo" role="img" aria-label="Photograph of the compact white whole slide scanner with front slide slot"></div>

    <div class="tissue-band tissue-band--bottom" role="img" aria-label="Stained tissue section micrograph in pink and purple"></div>
  </main>
</body>
</html>
```